Driftwood Coatings of Central Florida, LLC. Start-up painting business needs a professional web desig

We have a start up painting business that would like to reach/focus on commercial clients like building contractors, HOA's, apartment complexes, etc.. We would like a residential aspect to the web design as well. We have an existing website at "trydriftwoodcoatings.com" with usable content. Have logo and color scheme attached. Use provided website ONLY as template. Add commercial services page. Can type own content when needed.

```html
<!DOCTYPE html>
<html lang="en">
<head>
<meta charset="utf-8">
<title>Commercial Services – Driftwood Coatings of Central Florida, LLC</title>
<link rel="stylesheet" href="https://fonts.googleapis.com/css2?family=Didact+Gothic&family=Montserrat:ital,wght@0,700;1,800&display=swap">
<style>
:root{
  --wood-light:#e6ddd2;
  --wood-light-2:#d4c8bb;
  --wood-orange:#c9662c;
  --wood-orange-2:#a94f1f;
  --salmon:#e09a82;
  --salmon-deep:#d98a70;
  --olive:#5d5f22;
  --ink:#2f2f2f;
  --band:#2b2b2b;
  --teal:#6f9ba3;
  --mauve:#7a6a7a;
  --yellow:#f2c21a;
  --white:#ffffff;
  --text:#3a3a3a;
}
*{box-sizing:border-box;margin:0;padding:0}
html,body{width:1200px;height:2969px;overflow:hidden}
body{
  position:relative;
  font-family:"Didact Gothic",sans-serif;
  color:var(--text);
  background:
    linear-gradient(180deg,var(--wood-light) 0,var(--wood-light-2) 1000px,var(--wood-orange) 1090px,var(--wood-orange-2) 2969px);
}
.plank-lines{position:absolute;inset:0;pointer-events:none}
.abs{position:absolute}

/* header */
.brand{left:40px;top:14px;width:200px;display:flex;align-items:center;gap:10px}
.brand-mark{width:34px;height:34px;border-radius:50%;background:var(--salmon);flex:none}
.brand-name{font-size:13px;line-height:1.2;color:var(--olive)}
.nav a{position:absolute;font-size:17px;line-height:1.15;color:var(--ink);text-decoration:none;text-align:center;text-transform:uppercase}
.nav .active{color:var(--white)}
.active-tab{left:732px;top:0;width:151px;height:238px}
.phones{left:940px;top:14px;font-size:20px;line-height:24px;color:var(--ink)}
.phones svg{position:absolute;left:-34px;top:6px}

/* page panel */
.panel{left:82px;top:210px;width:1039px;height:2697px;background:var(--white)}
.intro{left:82px;width:1039px;top:280px;text-align:center}
.intro .lead{font-size:30px;letter-spacing:.5px;color:var(--ink)}
.intro .strong{font-family:"Montserrat",sans-serif;font-weight:800;font-style:italic;font-size:36px;color:var(--olive);letter-spacing:1px;margin-top:2px}

.collage{left:148px;top:438px}
.collage-title{left:382px;top:520px;font-size:32px;line-height:38px;color:var(--white)}

.section-bg{left:0;top:0}
.section-title{left:82px;width:1039px;top:1196px;text-align:center;font-size:38px;color:var(--salmon)}
.section-rule{left:520px;top:1250px;width:165px;height:4px;background:var(--salmon)}

/* service circles */
.service{
  position:absolute;border-radius:50%;border:12px solid var(--salmon);
  overflow:hidden;display:flex;flex-direction:column;align-items:center;
  color:var(--white);text-align:center;
}
.service .shade{position:absolute;inset:0;background:rgba(40,40,40,.45)}
.service .inner{position:relative;display:flex;flex-direction:column;align-items:center;width:100%;padding:0 56px}
.service-icon{width:40px;height:40px;border-radius:50%;background:var(--band);display:flex;align-items:center;justify-content:center}
.service h3{font-weight:400;font-size:30px;line-height:32px;margin-top:6px;text-transform:uppercase}
.service .rule{width:100px;height:5px;margin:8px 0 14px}
.service p{font-size:16px;line-height:19px;text-align:justify;text-align-last:center}

.hoa{left:88px;top:1345px;width:490px;height:490px;background:linear-gradient(160deg,#b9c4cb 0,#8c8a80 45%,#5f5c55 100%)}
.hoa .inner{margin-top:78px}
.hoa .rule{background:var(--white)}
.office{left:630px;top:1272px;width:478px;height:478px;background:linear-gradient(150deg,#d9dfe2 0,#c98b3e 45%,#7b5a3c 100%)}
.office .inner{margin-top:22px}
.office .rule{height:0;margin:4px 0 8px}
.contractors{left:136px;top:1990px;width:470px;height:470px;background:linear-gradient(160deg,#8e8e8a 0,#6f7274 50%,#c5472f 100%)}
.contractors .inner{margin-top:56px}
.contractors .rule{background:var(--yellow)}
.residential{left:643px;top:1903px;width:470px;height:470px;background:linear-gradient(160deg,#6e7f95 0,#b8423a 55%,#8a2f2a 100%)}
.residential .inner{margin-top:14px;padding:0 40px}
.residential .rule{background:var(--yellow)}

.contact-cta{left:82px;width:1039px;top:1858px;text-align:center;color:var(--white)}
.contact-cta .label{font-size:30px;color:var(--yellow);margin-left:-280px}
.contact-cta .num{font-size:30px;line-height:36px;margin-left:-280px}

/* footer */
.footer-brand{left:480px;width:240px;top:2480px;text-align:center}
.footer-brand .brand-mark{width:60px;height:60px;margin:0 auto 14px}
.footer-brand .brand-name{font-size:14px;line-height:17px;color:var(--ink);text-transform:uppercase}
.footer-nav{left:82px;width:1039px;top:2632px;text-align:center;font-size:12px;color:var(--ink);text-transform:uppercase}
.footer-nav span{margin:0 6px}
.social{left:500px;top:2680px;display:flex;gap:12px}
.social i{display:block;width:34px;height:34px;border-radius:4px}
.copyright{left:0;width:1200px;top:2918px;text-align:center;font-size:10px;color:var(--white);letter-spacing:.5px}
</style>
</head>
<body>

<svg class="plank-lines" width="1200" height="2969" aria-hidden="true">
  <g stroke="#c2b5a6" stroke-width="2" opacity=".6">
    <line x1="40" y1="0" x2="40" y2="1060"/><line x1="160" y1="0" x2="160" y2="1060"/>
    <line x1="300" y1="0" x2="300" y2="1060"/><line x1="1160" y1="0" x2="1160" y2="1060"/>
  </g>
  <g stroke="#8c3f17" stroke-width="3" opacity=".6">
    <line x1="30" y1="1090" x2="30" y2="2969"/><line x1="1150" y1="1090" x2="1150" y2="2969"/>
    <line x1="0" y1="1090" x2="1200" y2="1090"/>
  </g>
</svg>

<header>
  <div class="abs brand">
    <span class="brand-mark"></span>
    <span class="brand-name">Driftwood Coatings of Central Florida, LLC</span>
  </div>
  <svg class="abs active-tab" viewBox="0 0 151 238" aria-hidden="true">
    <polygon points="0,0 151,0 151,205 0,238" fill="var(--salmon)"/>
  </svg>
  <nav class="nav">
    <a href="#" style="left:312px;top:110px">Home</a>
    <a href="#" style="left:446px;top:110px">About Us</a>
    <a href="#" style="left:580px;top:110px;width:104px">Residential<br>Services</a>
    <a href="#" class="active" style="left:738px;top:110px;width:140px">Commercial<br>Services</a>
    <a href="#" style="left:948px;top:110px">Contact Us</a>
  </nav>
  <div class="abs phones">
    <svg width="26" height="26" viewBox="0 0 26 26" aria-hidden="true"><circle cx="13" cy="13" r="11" fill="none" stroke="var(--ink)" stroke-width="2"/><path d="M9 7c-1 1-1 3 1 6s4 5 6 5l1-2-2-2-2 1-3-3 1-2-2-3z" fill="var(--ink)"/></svg>
    +1.863-555-0142<br>+1.863-555-0187
  </div>
</header>

<main>
  <div class="abs panel"></div>

  <div class="abs intro">
    <div class="lead">WE OFFER A WIDE VARIETY OF SERVICES</div>
    <div class="strong">TO MEET ALL YOUR NEEDS</div>
  </div>

  <svg class="abs collage" width="904" height="570" viewBox="0 0 904 570">
    <g role="img" aria-label="Photo collage of homes, offices and painting work">
      <polygon points="0,0 223,0 223,300 0,310" fill="#7fa3c9"/>
      <polygon points="0,310 223,300 223,560 0,570" fill="#3f5a73"/>
      <polygon points="223,300 446,290 446,535 223,560" fill="#d9d4cc"/>
      <polygon points="446,0 668,0 668,285 446,290" fill="#b9a43a"/>
      <polygon points="446,290 668,285 668,500 446,535" fill="#8e8a6a"/>
      <polygon points="668,0 904,0 904,270 668,285" fill="#a8b6a0"/>
      <polygon points="668,285 904,220 904,460 668,500" fill="#3a5ea8"/>
    </g>
    <polygon points="223,0 446,0 446,290 223,300" fill="var(--salmon)"/>
  </svg>
  <div class="abs collage-title">COMMERCIAL<br>SERVICES</div>

  <svg class="abs section-bg" width="1200" height="2969" aria-hidden="true">
    <polygon points="82,1190 1121,1110 1121,2420 82,2478" fill="var(--band)"/>
    <polygon points="82,1392 1121,1282 1121,1760 82,1720" fill="var(--teal)" opacity=".75"/>
    <polygon points="82,2010 1121,1960 1121,2405 82,2445" fill="var(--mauve)" opacity=".75"/>
  </svg>

  <h2 class="abs section-title" style="font-weight:400">COMMERCIAL SERVICES</h2>
  <div class="abs section-rule"></div>

  <article class="service hoa" role="img" aria-label="Photo of a suburban home in an HOA community">
    <div class="shade"></div>
    <div class="inner">
      <span class="service-icon"><svg width="22" height="22" viewBox="0 0 22 22"><path d="M3 12 12 3M6 16 16 6M10 19 19 10" stroke="#fff" stroke-width="3"/></svg></span>
      <h3>HOA's</h3>
      <span class="rule"></span>
      <p>We don't just paint homes we paint communities. Come see what we could offer your community with our great exclusive contract deals. Give us a call for any individual service and we will make sure it is HOA approved before proceeding. Remember we are not just painters we're your neighbors.</p>
    </div>
  </article>

  <article class="service office" role="img" aria-label="Photo of a modern office interior">
    <div class="shade"></div>
    <div class="inner">
      <span class="service-icon"><svg width="22" height="22" viewBox="0 0 22 22"><path d="M3 12 12 3M6 16 16 6M10 19 19 10" stroke="#fff" stroke-width="3"/></svg></span>
      <h3>Office<br>Services</h3>
      <span class="rule"></span>
      <p>Need your office painted but can't close down to have it done? This is a problem faced by many business owners where one day closed can mean a lot of revenue lost. We can help alleviate all these problems with our evening or night painting services. We guarantee your customers will only see the new paint not the painters.</p>
    </div>
  </article>

  <div class="abs contact-cta">
    <div class="label">CONTACT US TODAY!</div>
    <div class="num">+1.863-555-0142</div>
    <div class="num">+1.863-555-0187</div>
  </div>

  <article class="service contractors" role="img" aria-label="Photo of construction tools on a blueprint">
    <div class="shade"></div>
    <div class="inner">
      <span class="service-icon"><svg width="22" height="22" viewBox="0 0 22 22"><path d="M3 12 12 3M6 16 16 6M10 19 19 10" stroke="#fff" stroke-width="3"/></svg></span>
      <h3>Contractors<br>Services</h3>
      <span class="rule"></span>
      <p>Starting new construction and need a painting contractor? Our commercial service team is well equipped and experienced to take on any commercial project. Call us today and let us show you the difference when you choose us.</p>
    </div>
  </article>

  <article class="service residential" role="img" aria-label="Photo of an apartment community building">
    <div class="shade"></div>
    <div class="inner">
      <span class="service-icon"><svg width="22" height="22" viewBox="0 0 22 22"><path d="M3 12 12 3M6 16 16 6M10 19 19 10" stroke="#fff" stroke-width="3"/></svg></span>
      <h3>Residential<br>Management Services</h3>
      <span class="rule"></span>
      <p>When it's time to choose the right painting contractor for your residential community you come to the right place. Inside or out we can provide all your painting project needs. With our experience and eye for detail you won't have to look for another painting service provider again! Need painting maintenance beyond what your maintenance personal can provide? Call today and we will find a plan that fits your residential communities needs.</p>
    </div>
  </article>
</main>

<footer>
  <div class="abs footer-brand">
    <div class="brand-mark"></div>
    <div class="brand-name">Driftwood Coatings of<br>Central Florida, LLC.</div>
  </div>
  <div class="abs footer-nav">Home<span>|</span>About Us<span>|</span>Services<span>|</span>Commercial Services<span>|</span>Contact Us</div>
  <div class="abs social" aria-label="Social links">
    <i style="background:#3b5998"></i><i style="background:#4aa8d8"></i><i style="background:#c8232c"></i><i style="background:#3f8f4a"></i>
  </div>
  <div class="abs copyright">COPYRIGHT © DRIFTWOOD COATINGS. ALL RIGHTS RESERVED</div>
</footer>

</body>
</html>
```